My Business is Car Dealership, we sale cars and trucks, I’m looking for a sign design
I need 2 signage
9ā€ by 7ā€ feet.
the other sign is 3" feet high and the width is 12" feet

For further reference about the company , you can check my website
www.harrowbayautosale.com

Industry/Entity Type

Business

Requirements
Must have
• picture of 2018 marlo K240 or 2018 Vantrelle Duskmoor
Nice to have
• the business name Harrow Bay Auto Sale visible from far distance

```html
<!DOCTYPE html>
<html lang="en">
<head>
<meta charset="utf-8">
<title>Harrow Bay Auto Sale – Sign</title>
<link rel="stylesheet" href="https://fonts.googleapis.com/css2?family=Saira+Condensed:wght@600&family=Barlow+Semi+Condensed:ital,wght@1,800&family=Barlow:ital,wght@1,800&display=swap">
<style>
  :root {
    --canvas-bg: #e4e4e4;
    --sign-dark: #141414;
    --sign-mid: #232323;
    --brand-red: #d40000;
    --band-red-dark: #9c0000;
    --band-grey-top: #6a6a6a;
    --band-grey-bottom: #2e2e2e;
    --white: #ffffff;
    --silver: #bdbdbd;
  }
  html, body {
    margin: 0;
    padding: 0;
    width: 1200px;
    height: 1029px;
    overflow: hidden;
    background: var(--canvas-bg);
  }
  .sign {
    position: absolute;
    left: 0;
    top: 48px;
    width: 1200px;
    height: 932px;
    background: radial-gradient(ellipse at 50% 40%, var(--sign-mid) 0%, var(--sign-dark) 75%);
    overflow: hidden;
  }
  .brand-mark {
    position: absolute;
    left: 600px;
    top: 160px;
    width: 0;
    height: 0;
  }
  .brand-mark svg {
    position: absolute;
    left: -115px;
    top: -115px;
  }
  .brand-name {
    position: absolute;
    left: 0;
    width: 1200px;
    top: 312px;
    text-align: center;
    font-family: "Saira Condensed", sans-serif;
    font-weight: 600;
    font-size: 104px;
    line-height: 1;
    letter-spacing: 1px;
    color: var(--brand-red);
  }
  .headline {
    position: absolute;
    left: 0;
    width: 1200px;
    text-align: center;
    font-family: "Barlow Semi Condensed", sans-serif;
    font-weight: 800;
    font-style: italic;
    font-size: 116px;
    line-height: 1;
    color: var(--white);
    background: linear-gradient(180deg, var(--white) 45%, var(--silver) 100%);
    -webkit-background-clip: text;
    background-clip: text;
    -webkit-text-fill-color: transparent;
    filter: drop-shadow(4px 4px 0 var(--brand-red));
  }
  .headline--top { top: 440px; }
  .headline--bottom { top: 562px; }
  .call-band {
    position: absolute;
    left: 0;
    top: 698px;
    width: 1200px;
    height: 112px;
  }
  .call-band svg { position: absolute; left: 0; top: 0; }
  .call-text {
    position: absolute;
    left: 0;
    width: 1200px;
    top: 12px;
    text-align: center;
    font-family: "Barlow Semi Condensed", sans-serif;
    font-weight: 800;
    font-style: italic;
    font-size: 88px;
    line-height: 1;
    color: var(--white);
    text-shadow: 3px 3px 0 var(--brand-red);
  }
  .web-band {
    position: absolute;
    left: 0;
    top: 810px;
    width: 1200px;
    height: 122px;
    background: linear-gradient(90deg, var(--brand-red) 0%, var(--band-red-dark) 100%);
  }
  .web-text {
    position: absolute;
    left: 0;
    width: 1200px;
    top: 24px;
    text-align: center;
    font-family: "Barlow", sans-serif;
    font-weight: 800;
    font-style: italic;
    font-size: 62px;
    line-height: 1;
    color: var(--white);
    text-shadow: 4px 4px 0 #000;
  }
</style>
</head>
<body>
  <main class="sign">
    <div class="brand-mark" aria-hidden="true">
      <svg width="230" height="230" viewBox="0 0 230 230">
        <circle cx="115" cy="115" r="104" fill="none" stroke="var(--brand-red)" stroke-width="12"/>
      </svg>
    </div>
    <div class="brand-name">Harrow Bay Auto Sale</div>

    <div class="headline headline--top">CAR DEALERSHIP</div>
    <div class="headline headline--bottom">CAR SALES</div>

    <div class="call-band">
      <svg width="1200" height="112" viewBox="0 0 1200 112" aria-hidden="true">
        <defs>
          <linearGradient id="callBandFill" x1="0" y1="0" x2="0" y2="1">
            <stop offset="0" stop-color="var(--band-grey-top)"/>
            <stop offset="1" stop-color="var(--band-grey-bottom)"/>
          </linearGradient>
        </defs>
        <polygon points="112,0 1088,0 1112,112 88,112" fill="url(#callBandFill)"/>
      </svg>
      <div class="call-text">CALL - 555-302-7714</div>
    </div>

    <div class="web-band">
      <div class="web-text">www.harrowbayautosale.com</div>
    </div>
  </main>
</body>
</html>
```